Take my logo and make me some cool looking business cards

I've got a logo that we've trademarked so you can't change the logo but you can change it's color combo and find a fun way to incorporate it into a new business card design that is fresh, stylish, and can be applied to some cool medium cost materials (plastic, wood, metal, etc). Basically, we're looking for business cards that stand out in a good way.
Here's the logo we're currently using:
Thanks to everyone that has submitted designs. We've narrowed down to the top 4 designs and tried to eliminate old versions or designs that just didn't match our vision as quickly as we could. We don't plan on keeping this open for the full 9 days; we plan on selecting a design in the next 48 hours; with the goal of having something in the hands of a printer, preferably plastic printer, by Thursday AM Pacific Time.
Business
- must include our existing logo

```html
<!DOCTYPE html>
<html lang="en">
<head>
<meta charset="utf-8">
<title>Tetherline Business Cards</title>
<link href="https://fonts.googleapis.com/css2?family=Open+Sans:wght@400;600;700&display=swap" rel="stylesheet">
<style>
  :root {
    --brand-blue: #1756a9;
    --band-dark: #3a3a3c;
    --card-white: #ffffff;
    --ink-grey: #5a5d63;
    --backdrop: #d9d6d8;
    --plastic-a: #d9b42a;
    --plastic-b: #7a3f4e;
    --wood-a: #c98a2e;
    --wood-b: #8a5418;
    --metal-a: #e6e7e9;
    --metal-b: #a9abae;
  }
  * { margin: 0; padding: 0; box-sizing: border-box; }
  html, body { width: 1200px; height: 999px; overflow: hidden; }
  body {
    background: var(--backdrop);
    font-family: "Open Sans", Arial, sans-serif;
    display: flex;
    align-items: center;
    justify-content: center;
    gap: 60px;
  }
  .card {
    position: relative;
    width: 520px;
    height: 300px;
    background: var(--card-white);
    box-shadow: 0 6px 20px rgba(0,0,0,0.18);
    overflow: hidden;
  }
  .card-bands { position: absolute; inset: 0; }
  .brand-name {
    position: absolute;
    left: 34px;
    top: 70px;
    font-weight: 600;
    font-size: 44px;
    letter-spacing: 3px;
    color: var(--brand-blue);
  }
  .contact-list {
    position: absolute;
    left: 34px;
    top: 150px;
    list-style: none;
    font-size: 12px;
    color: var(--ink-grey);
    line-height: 19px;
  }
  .contact-list li { display: flex; align-items: center; gap: 8px; }
  .contact-list svg { width: 11px; height: 11px; fill: var(--brand-blue); }
  .web-address {
    position: absolute;
    right: 34px;
    bottom: 16px;
    display: flex;
    align-items: center;
    gap: 8px;
    font-size: 15px;
    color: var(--card-white);
  }
  .web-address svg { width: 15px; height: 15px; }
  .materials {
    position: absolute;
    left: 26px;
    top: 58px;
    display: flex;
    gap: 22px;
  }
  .material { display: flex; flex-direction: column; align-items: center; gap: 8px; }
  .material-swatch { width: 140px; height: 128px; }
  .swatch-plastic { background: linear-gradient(135deg, var(--plastic-b) 0%, #3f5fa0 40%, var(--plastic-a) 75%); }
  .swatch-wood { background: linear-gradient(160deg, var(--wood-a), var(--wood-b)); }
  .swatch-metal { background: linear-gradient(135deg, var(--metal-a), var(--metal-b)); }
  .material-label {
    font-weight: 700;
    font-size: 17px;
    letter-spacing: 1px;
    color: var(--brand-blue);
  }
</style>
</head>
<body>

  <section class="card card-back">
    <svg class="card-bands" viewBox="0 0 520 300" aria-hidden="true">
      <path d="M300 24 H520 V50 H334 Q320 50 314 42 Z" fill="var(--band-dark)"/>
      <path d="M0 0 H520 V40 H336 Q322 40 316 32 L310 24 H0 Z" fill="var(--brand-blue)"/>
      <path d="M0 246 H236 L228 264 H0 Z" fill="var(--band-dark)"/>
      <path d="M0 300 V268 H206 Q218 268 224 260 L232 250 H520 V300 Z" fill="var(--brand-blue)"/>
    </svg>
    <div class="materials">
      <div class="material">
        <div class="material-swatch swatch-plastic" role="img" aria-label="Photo of colourful interlocking plastic floor tiles"></div>
        <span class="material-label">PLASTIC</span>
      </div>
      <div class="material">
        <div class="material-swatch swatch-wood" role="img" aria-label="Photo of golden wooden deck planks"></div>
        <span class="material-label">WOOD</span>
      </div>
      <div class="material">
        <div class="material-swatch swatch-metal" role="img" aria-label="Photo of silver diamond plate metal"></div>
        <span class="material-label">METAL</span>
      </div>
    </div>
  </section>

  <section class="card card-front">
    <svg class="card-bands" viewBox="0 0 520 300" aria-hidden="true">
      <path d="M300 24 H520 V50 H334 Q320 50 314 42 Z" fill="var(--band-dark)"/>
      <path d="M0 0 H520 V40 H336 Q322 40 316 32 L310 24 H0 Z" fill="var(--brand-blue)"/>
      <path d="M0 246 H236 L228 264 H0 Z" fill="var(--band-dark)"/>
      <path d="M0 300 V268 H206 Q218 268 224 260 L232 250 H520 V300 Z" fill="var(--brand-blue)"/>
    </svg>
    <div class="brand-name">TETHERLINE</div>
    <ul class="contact-list">
      <li><svg viewBox="0 0 12 12"><path d="M2 1 L4.5 1 L5.5 3.5 L4 4.8 Q5 7 7.2 8 L8.5 6.5 L11 7.5 L11 10 Q6 11 2.5 7 Q1 4.5 2 1 Z"/></svg>: 555 0142 7781</li>
      <li><svg viewBox="0 0 12 12"><circle cx="6" cy="3.5" r="2.5"/><path d="M1 11 Q1 6.5 6 6.5 Q11 6.5 11 11 Z"/></svg>: 555 0142 7782</li>
      <li><svg viewBox="0 0 12 12"><path d="M1 2.5 H11 V9.5 H1 Z M1.5 3 L6 6.5 L10.5 3" fill="none" stroke="var(--brand-blue)" stroke-width="1.2"/></svg>: hello@tetherline.co</li>
    </ul>
    <div class="web-address">
      <svg viewBox="0 0 16 16" fill="none" stroke="#fff" stroke-width="1.2"><circle cx="8" cy="8" r="6.5"/><ellipse cx="8" cy="8" rx="3" ry="6.5"/><path d="M1.5 8 H14.5 M2.5 4.8 H13.5 M2.5 11.2 H13.5"/></svg>
      <span>: tetherline.co</span>
    </div>
  </section>

</body>
</html>
```